Surviving Domestic Violence Flyer

I need a flyer that "POPS" to attract participants for my research project. I have added the important information on my draft flyer.

```html
<!DOCTYPE html>
<html lang="en">
<head>
<meta charset="utf-8">
<title>Request For Study Participants</title>
<link href="https://fonts.googleapis.com/css2?family=Barlow+Condensed:ital,wght@0,300;0,400;1,300&family=Open+Sans:wght@700&family=Source+Sans+3:wght@400&display=swap" rel="stylesheet">
<style>
  :root {
    --plum: #9b1d5e;
    --orange: #f26a23;
    --red: #c0262d;
    --deep-red: #8c1a22;
    --ink: #333333;
    --paper-top: #ececec;
    --paper-bottom: #ffffff;
    --white: #ffffff;
  }
  html, body {
    margin: 0;
    padding: 0;
    overflow: hidden;
    background: var(--white);
  }
  .flyer {
    position: relative;
    width: 927px;
    height: 1200px;
    overflow: hidden;
    background: linear-gradient(180deg, var(--paper-top) 0%, var(--paper-bottom) 45%, var(--paper-bottom) 100%);
  }
  .flyer__title {
    position: absolute;
    top: 62px;
    left: 50%;
    transform: translateX(-50%);
    margin: 0;
    white-space: nowrap;
    font-family: "Barlow Condensed", "Arial Narrow", sans-serif;
    font-style: italic;
    font-weight: 300;
    font-size: 84px;
    line-height: 1;
    color: var(--plum);
  }
  .flyer__subtitle {
    position: absolute;
    top: 180px;
    left: 0;
    width: 927px;
    margin: 0;
    text-align: center;
    font-family: "Open Sans", Arial, sans-serif;
    font-weight: 700;
    font-size: 22px;
    letter-spacing: 1px;
    line-height: 31px;
    color: var(--orange);
    text-transform: uppercase;
  }
  .criteria {
    position: absolute;
    top: 266px;
    left: 68px;
    width: 820px;
    margin: 0;
    padding: 0;
    list-style: none;
    font-family: "Barlow Condensed", "Arial Narrow", sans-serif;
    font-weight: 400;
    font-size: 31px;
    line-height: 37px;
    color: var(--ink);
    z-index: 2;
  }
  .criteria li {
    position: relative;
    padding-left: 19px;
  }
  .criteria li::before {
    content: "";
    position: absolute;
    left: 0;
    top: 16px;
    width: 7px;
    height: 7px;
    border-radius: 50%;
    background: var(--ink);
  }
  .hands-art,
  .band {
    position: absolute;
    left: 0;
    top: 0;
    width: 927px;
    height: 1200px;
    z-index: 1;
  }
  .details {
    position: absolute;
    left: 74px;
    top: 906px;
    width: 720px;
    font-family: "Source Sans 3", Arial, sans-serif;
    font-size: 18px;
    line-height: 21.5px;
    color: var(--white);
    z-index: 2;
  }
  .details p {
    margin: 0 0 21px 0;
  }
  .details .credits {
    margin-top: 28px;
  }
</style>
</head>
<body>
<div class="flyer">
  <h1 class="flyer__title">Request For Study Participants</h1>
  <h2 class="flyer__subtitle">Efficiency of resources available to survivors<br>of intimate partner abuse</h2>

  <ul class="criteria">
    <li>Are you eighteen years of age or older?</li>
    <li>Have you been a victim of domestic violence?</li>
    <li>Have you sought assistance with abuse in the last 12 months?</li>
    <li>Are you still in contact with the person who abused you?</li>
    <li>Are you willing and open to discussing your experience with<br>abuse and your attempts to access services or resources?</li>
  </ul>

  <svg class="hands-art" viewBox="0 0 927 1200" role="img" aria-label="Illustration of raised hands in red, orange and plum reaching upward">
    <defs>
      <linearGradient id="handsRight" x1="0" y1="0" x2="1" y2="1">
        <stop offset="0" stop-color="#c0262d" stop-opacity="0.55"/>
        <stop offset="0.5" stop-color="#f26a23" stop-opacity="0.55"/>
        <stop offset="1" stop-color="#9b1d5e" stop-opacity="0.55"/>
      </linearGradient>
      <linearGradient id="handsLeft" x1="0" y1="0" x2="1" y2="0">
        <stop offset="0" stop-color="#9b1d5e" stop-opacity="0.55"/>
        <stop offset="0.5" stop-color="#c0262d" stop-opacity="0.55"/>
        <stop offset="1" stop-color="#f26a23" stop-opacity="0.55"/>
      </linearGradient>
    </defs>
    <path d="M600 640 Q700 560 760 520 Q830 470 880 420 L927 400 L927 700 L560 760 Z" fill="url(#handsRight)"/>
    <path d="M30 580 L600 620 L600 800 L0 860 L0 600 Z" fill="url(#handsLeft)"/>
  </svg>

  <svg class="band" viewBox="0 0 927 1200" aria-hidden="true">
    <defs>
      <linearGradient id="bandFill" x1="0" y1="0" x2="0" y2="1">
        <stop offset="0" stop-color="#c0262d"/>
        <stop offset="1" stop-color="#8c1a22"/>
      </linearGradient>
    </defs>
    <path d="M0 842 C250 800 560 760 927 664 L927 1200 L0 1200 Z" fill="#d8454a" opacity="0.55"/>
    <path d="M0 860 C260 820 580 770 927 690 L927 1200 L0 1200 Z" fill="url(#bandFill)"/>
  </svg>

  <div class="details">
    <p>If you answered yes to all of these questions, you may be eligible to participate in a study to better understand the resources needed and services expected for survivors of domestic violence.</p>
    <p>Please contact Dana Whitfield at 1(555)014-2290 or via e-mail: ipa.resourcestudy@examplemail.com for additional information.</p>
    <p>Participants will be compensated for their time.</p>
    <p class="credits">Principal Investigator: Dana Whitfield<br>Institutional Affiliation: Lakeshore State University, Dept. of Criminology, Law, and Justice<br>Contact Address: Post Office Box 100482, Riverton, IL, 60000</p>
  </div>
</div>
</body>
</html>
```